Standard logo business card

We are seeking a solid, somewhat understated professional design. We are a tech company. We like fonts similar to Aptifer Slab. Front side will be white with the contact information and a small version of our primary (Light background) logo.

(We have three people so we will have three names and titles)

Back side will hold our reverse logo on dark background along with the tagline:

"Intelligent annotation solutions for complex data"

Target Market(s)

Professionals, Tech

Industry/Entity Type

Business

Contact Information for Business Card

Name
Title

Phone
Email
City, State
Website

[We will email leading designer specific contact information)

Font styles to use
Serif

Requirements
Must have
• Colors are:
• Orange RGB 245,92,23
• Blue RGB 3,34,56
Nice to have
• We like a split with the Name and Title on the right and then contact details (below) on the left.

```html
<!DOCTYPE html>
<html lang="en">
<head>
<meta charset="utf-8">
<title>Veltrana business card</title>
<link href="https://fonts.googleapis.com/css2?family=Roboto+Slab:wght@300;400;600&display=swap" rel="stylesheet">
<style>
  :root {
    --canvas: #e9e6e1;
    --card: #ffffff;
    --frame: #1c1c1e;
    --orange: rgb(245, 92, 23);
    --orange-soft: #f9a57f;
    --blue: rgb(3, 34, 56);
    --charcoal: #3a3a3d;
    --white: #ffffff;
    --mist: #c9d3dc;
  }
  * { box-sizing: border-box; margin: 0; padding: 0; }
  html, body { width: 1057px; height: 1200px; overflow: hidden; }
  body {
    background: var(--canvas);
    font-family: "Roboto Slab", serif;
    display: flex;
    align-items: center;
    justify-content: center;
    gap: 80px;
  }
  .card {
    width: 400px;
    height: 700px;
    border: 16px solid var(--frame);
    position: relative;
    overflow: hidden;
    box-shadow: 0 10px 30px rgba(0,0,0,.18);
  }
  .card-front { background: var(--card); }
  .card-back { background: var(--blue); }
  .brand {
    display: flex;
    align-items: center;
    gap: 12px;
    font-weight: 600;
    letter-spacing: -0.5px;
    line-height: 1;
  }
  .brand-square { background: var(--orange); flex: none; }
  .card-front .brand {
    position: absolute; top: 100px; left: 0; right: 0;
    justify-content: center; font-size: 48px; color: var(--blue);
  }
  .card-front .brand-square { width: 22px; height: 22px; }
  .person { position: absolute; top: 228px; left: 40px; }
  .person-name {
    font-weight: 300; font-size: 28px; letter-spacing: 2px;
    text-transform: uppercase; color: var(--blue); line-height: 1.2;
  }
  .person-title {
    font-weight: 300; font-size: 13px; letter-spacing: 2px;
    text-transform: uppercase; color: var(--blue);
    border-top: 1px solid var(--blue); padding-top: 5px; margin-top: 3px;
  }
  .contact-band {
    position: absolute; left: 0; right: 0; top: 318px; height: 238px;
    background: var(--orange);
    border-top: 10px solid var(--orange-soft);
    padding: 30px 36px;
    display: flex; flex-direction: column; gap: 20px;
  }
  .contact-row { display: flex; align-items: center; gap: 16px; color: var(--white); font-size: 15px; }
  .icon {
    width: 26px; height: 26px; border-radius: 5px; background: var(--white);
    display: flex; align-items: center; justify-content: center; flex: none;
  }
  .icon svg { width: 16px; height: 16px; }
  .address-band {
    position: absolute; left: 0; right: 0; bottom: 0; height: 112px;
    background: var(--charcoal);
    display: flex; align-items: center; gap: 16px; padding: 0 36px;
    color: var(--white); font-size: 13px; white-space: nowrap;
  }
  .back-content {
    position: absolute; inset: 0;
    display: flex; flex-direction: column; align-items: center; justify-content: center;
    gap: 26px; padding: 0 40px;
  }
  .card-back .brand { font-size: 54px; color: var(--white); }
  .card-back .brand-square { width: 28px; height: 28px; }
  .tagline {
    font-weight: 300; font-size: 15px; line-height: 1.5;
    color: var(--mist); text-align: center; letter-spacing: .3px;
    max-width: 280px;
  }
</style>
</head>
<body>
  <section class="card card-front" aria-label="Front of card">
    <div class="brand"><span class="brand-square"></span>Veltrana</div>
    <div class="person">
      <p class="person-name">Mara Ellison</p>
      <p class="person-title">General Manager</p>
    </div>
    <div class="contact-band">
      <div class="contact-row">
        <span class="icon"><svg viewBox="0 0 16 16"><path d="M4 1.5l2.5 3-1.5 1.6c.8 1.8 2.2 3.2 4 4l1.6-1.5 3 2.5-1.4 2.4C7 13 3 9 1.6 3z" fill="var(--orange)"/></svg></span>
        <span>012 555 0147</span>
      </div>
      <div class="contact-row">
        <span class="icon"><svg viewBox="0 0 16 16"><rect x="4" y="1" width="8" height="14" rx="1.5" fill="var(--orange)"/><rect x="5.5" y="3" width="5" height="8" fill="var(--white)"/></svg></span>
        <span>012 555 0148</span>
      </div>
      <div class="contact-row">
        <span class="icon"><svg viewBox="0 0 16 16"><rect x="1" y="3" width="14" height="10" rx="1" fill="var(--orange)"/><path d="M1.5 3.5L8 9l6.5-5.5" stroke="var(--white)" stroke-width="1.3" fill="none"/></svg></span>
        <span>hello@veltrana.com</span>
      </div>
      <div class="contact-row">
        <span class="icon"><svg viewBox="0 0 16 16"><circle cx="8" cy="8" r="6.5" fill="none" stroke="var(--orange)" stroke-width="1.6"/><path d="M1.5 8h13M8 1.5c-3 3.5-3 9.5 0 13M8 1.5c3 3.5 3 9.5 0 13" stroke="var(--orange)" stroke-width="1.1" fill="none"/></svg></span>
        <span>www.veltrana.com</span>
      </div>
    </div>
    <div class="address-band">
      <span class="icon"><svg viewBox="0 0 16 16"><path d="M8 1a5 5 0 0 0-5 5c0 3.8 5 9 5 9s5-5.2 5-9a5 5 0 0 0-5-5z" fill="var(--charcoal)"/><circle cx="8" cy="6" r="1.8" fill="var(--white)"/></svg></span>
      <span>42 Harbor Lane, 3rd Floor, Suite 7</span>
    </div>
  </section>

  <section class="card card-back" aria-label="Back of card">
    <div class="back-content">
      <div class="brand"><span class="brand-square"></span>Veltrana</div>
      <p class="tagline">Intelligent annotation solutions for complex data</p>
    </div>
  </section>
</body>
</html>
```